" Empresa jurídica moderna e atuante com foco no segmento empresarial, conta com diferencial de propor uma maior aproximaçao com as empresas/clientes, solucionando seus problemas e prevendo suas necessidades. "

```html
<!DOCTYPE html>
<html lang="pt-BR">
<head>
<meta charset="utf-8">
<title>Moraes, Teixeira &amp; Almeida — Envelopes</title>
<link href="https://fonts.googleapis.com/css2?family=Cormorant+Garamond:wght@500&family=Lato:wght@400&display=swap" rel="stylesheet">
<style>
  :root {
    --page-bg: #e7e6e3;
    --navy: #2c4373;
    --paper: #ffffff;
    --ink: #4a5670;
    --ink-soft: #8a93a6;
    --rule: #d7d9de;
  }
  * { margin: 0; padding: 0; box-sizing: border-box; }
  html, body { width: 1200px; height: 1200px; overflow: hidden; }
  body { background: var(--page-bg); position: relative; font-family: "Lato", sans-serif; }

  .envelope { position: absolute; top: 245px; width: 497px; height: 708px; box-shadow: 0 6px 18px rgba(0,0,0,.18); }

  /* Back of envelope */
  .envelope--back { left: 86px; background: var(--navy); overflow: hidden; }
  .envelope__opening { position: absolute; left: 0; top: 0; }
  .back-brand { position: absolute; left: 0; right: 0; top: 122px; text-align: center; color: var(--paper); }
  .back-brand__mark { display: block; width: 30px; height: 30px; margin: 0 auto 8px; background: var(--paper); opacity: .9; }
  .back-brand__name { font-family: "Cormorant Garamond", serif; font-weight: 500; font-size: 17px; letter-spacing: .5px; }
  .back-brand__tagline { font-size: 6px; letter-spacing: 1.6px; text-transform: uppercase; opacity: .8; margin-top: 3px; border-top: 1px solid rgba(255,255,255,.4); display: inline-block; padding-top: 3px; }
  .back-contact { position: absolute; left: 12px; bottom: 14px; color: var(--paper); font-size: 8px; line-height: 12px; opacity: .9; }
  .back-contact__web { font-weight: 400; }

  /* Front of envelope */
  .envelope--front { left: 603px; background: var(--paper); }
  .front-rule { position: absolute; left: 48px; right: 48px; height: 1px; background: var(--rule); }
  .front-rule--top { top: 43px; }
  .front-rule--bottom { bottom: 40px; }
  .front-brand { position: absolute; left: 0; right: 0; top: 300px; text-align: center; color: var(--ink); }
  .front-brand__mark { display: block; width: 48px; height: 48px; margin: 0 auto 12px; background: var(--navy); }
  .front-brand__name { font-family: "Cormorant Garamond", serif; font-weight: 500; font-size: 33px; letter-spacing: .5px; line-height: 1; }
  .front-brand__tagline { display: inline-block; margin-top: 8px; padding-top: 6px; border-top: 1px solid var(--ink-soft); font-size: 9px; letter-spacing: 3px; text-transform: uppercase; color: var(--ink-soft); }
</style>
</head>
<body>
  <section class="envelope envelope--back" aria-label="Verso do envelope">
    <svg class="envelope__opening" width="497" height="100" viewBox="0 0 497 100" aria-hidden="true">
      <path d="M14 0 H483 V70 Q483 92 461 92 H36 Q14 92 14 70 Z" fill="#ffffff"/>
    </svg>
    <div class="back-brand">
      <span class="back-brand__mark"></span>
      <div class="back-brand__name">MORAES, TEIXEIRA &amp; ALMEIDA</div>
      <div class="back-brand__tagline">Advocacia e Consultoria Jurídica</div>
    </div>
    <address class="back-contact" style="font-style:normal">
      Rua Exemplo das Flores, 100<br>
      Bairro Centro | Cidade/SP<br>
      CEP 00000-000<br>
      Tel: (11) 0000-0000<br>
      <span class="back-contact__web">www.mtaadvocacia.com.br</span>
    </address>
  </section>

  <section class="envelope envelope--front" aria-label="Frente do envelope">
    <div class="front-rule front-rule--top"></div>
    <div class="front-brand">
      <span class="front-brand__mark"></span>
      <div class="front-brand__name">MORAES, TEIXEIRA &amp; ALMEIDA</div>
      <div class="front-brand__tagline">Advocacia e Consultoria Jurídica</div>
    </div>
    <div class="front-rule front-rule--bottom"></div>
  </section>
</body>
</html>
```